Property Management Firm Introduces New Programs

4 pages, 5.5 x 8.5 finished size, 4-color
We are introducing two new programs: Financial Management and Q-Steward. These programs are more affordable than full-service management. The brochure should come across as professional but not too glossy to give the impression of affordability coupled with stability and reliability. That said, we like to have a little fun with what we do--or it's not worth doing.

Target Market(s)

self-managed HOA and condo association

Industry/Entity Type

Real Estate

Other font styles liked:
• Trocchi, Activ Grotesk

Requirements
Must have
• Easy to read
• Our corporate fonts are Trocchi and Aktiv Grotesk
• Let me know if you need me to upload those fonts.
• LOGO Colors
• Red / Green / Blue
• Cyan 27 84 74
• Magenta 98 25 75
• Yellow 81 96 3
• Black 49 28 85
Nice to have
• The content is submitted in a rough design format to give you an idea of what we are looking for. I've attached the photos used in the design. Am open to the idea of different photos. This has a tight deadline so trying to give as much as possible

```html
<!DOCTYPE html>
<html lang="en">
<head>
<meta charset="utf-8">
<title>Financial Management and Q-Steward</title>
<link rel="stylesheet" href="https://fonts.googleapis.com/css2?family=Montserrat:wght@600;700;800&family=Hind:wght@400;600&display=swap">
<style>
  :root {
    --surround: #5a5a5c;
    --paper: #ffffff;
    --paper-shade: #e6e6e8;
    --wine: #6e1221;
    --wine-light: #9a3a44;
    --leaf: #2f7d3b;
    --navy: #2f3f8f;
    --steel: #b4b5b8;
    --ink: #3a3a3c;
    --photo-light: #dfe6ef;
    --photo-mid: #9fb0c6;
    --photo-dark: #4c6280;
  }
  * { box-sizing: border-box; margin: 0; padding: 0; }
  html, body { width: 852px; height: 1200px; overflow: hidden; }
  body { background: var(--surround); position: relative; font-family: "Hind", sans-serif; }

  .flyer {
    position: absolute; left: 119px; top: 125px; width: 614px; height: 951px;
    background: linear-gradient(90deg, var(--paper-shade) 0%, var(--paper) 45%);
    overflow: hidden;
  }
  .hero { position: absolute; left: 0; top: 0; width: 614px; height: 380px; }

  .headline {
    position: absolute; left: 34px; top: 312px;
    font-family: "Montserrat", sans-serif; font-weight: 700;
    font-size: 50px; line-height: 49px; letter-spacing: -1px; color: var(--wine);
  }
  .intro-line {
    position: absolute; left: 34px; top: 422px; width: 545px;
    font-family: "Montserrat", sans-serif; font-weight: 600;
    font-size: 18.5px; color: var(--leaf); white-space: nowrap;
  }
  .program-name {
    position: absolute; left: 34px; top: 470px; width: 545px;
    font-family: "Montserrat", sans-serif; font-weight: 800;
    font-size: 76px; line-height: 110px; letter-spacing: -1px;
    color: var(--steel); white-space: nowrap;
  }
  .audience-line {
    position: absolute; left: 34px; top: 601px; width: 560px;
    font-family: "Montserrat", sans-serif; font-weight: 700;
    font-size: 28.5px; color: var(--wine); white-space: nowrap;
  }

  .copy { position: absolute; left: 34px; top: 652px; width: 548px; color: var(--ink); }
  .copy h2 { font-family: "Hind", sans-serif; font-weight: 600; font-size: 14px; line-height: 17px; color: #2d2d2f; }
  .copy p { font-size: 13px; line-height: 17px; text-align: justify; }
  .copy .block { margin-bottom: 11px; }

  .foot-band {
    position: absolute; left: 0; bottom: 0; width: 614px; height: 17px;
    background: linear-gradient(90deg, var(--wine-light) 0%, var(--wine) 35%, var(--wine) 100%);
  }
</style>
</head>
<body>
  <main class="flyer">
    <svg class="hero" viewBox="0 0 614 380" aria-hidden="false">
      <defs>
        <linearGradient id="photoTone" x1="0" y1="0" x2="1" y2="1">
          <stop offset="0" stop-color="var(--photo-dark)"/>
          <stop offset="0.45" stop-color="var(--photo-mid)"/>
          <stop offset="1" stop-color="var(--photo-light)"/>
        </linearGradient>
      </defs>
      <path role="img" aria-label="Photo of a calculator keypad beside stacked coins on a financial chart printout"
            d="M0 0 H614 V295 C540 320 470 305 380 290 C260 265 160 215 0 255 Z" fill="url(#photoTone)"/>
      <path d="M0 255 C160 215 260 265 380 290 C470 305 540 320 614 295" fill="none" stroke="var(--navy)" stroke-width="12"/>
      <path d="M0 273 C150 238 270 283 380 304 C470 320 545 333 614 312" fill="none" stroke="var(--wine)" stroke-width="7"/>
      <path d="M0 287 C150 256 270 296 380 318 C470 334 545 345 614 322" fill="none" stroke="var(--leaf)" stroke-width="4"/>
      <path d="M385 335 C470 350 545 357 614 338" fill="none" stroke="var(--wine)" stroke-width="3"/>
    </svg>

    <h1 class="headline">Financial<br>Management</h1>
    <p class="intro-line">FOR COMMUNITY ASSOCIATIONS AND INTRODUCING</p>
    <p class="program-name">Q-STEWARD</p>
    <p class="audience-line">FOR SELF-MANAGED ASSOCIATIONS</p>

    <section class="copy">
      <div class="block">
        <h2>SIZE DOESNOT MATTER...</h2>
        <p>Whether small or large, your association needs to make the best use of the free volunteer resources and on-site staff you have within your community.</p>
      </div>
      <div class="block">
        <h2>Smaller Communities</h2>
        <p>Crestline financial management delivers the same accounting functionality received by our full-service communities at a fraction of the full-serve price.</p>
      </div>
      <div class="block">
        <h2>Larger Communities</h2>
        <p>Maybe you feel your active Board—even an on-site manager—is best focused on your facilities where you can make the most difference. Maybe none of them are accountants and you don’t want to purchase expensive software.</p>
      </div>
      <div class="block">
        <p>Our objective is to deliver impeccable financial management, and, where applicable, provide you online access to self-management tools that can make your management tasks and communications with residents so much easier!</p>
      </div>
    </section>

    <div class="foot-band"></div>
  </main>
</body>
</html>
```